Thornfield Visa Group Business Card

Boston based immigration and tax law firm.
Will serve wealthy individuals who wish to immigrate to the US.
Colors as in Logo, blue white.
Delivering sophisticated legal services.
Attached please see logo design from website.
Target Market(s)
non-US citizens
Industry/Entity Type
Legal
Contact Information for Business Card
Gerald T. Hensworth, Esq. LL.M, M.Sc., M.Fin
Thornfield Visa Group LLC
47 Kessel Ave., #218
Boston, MA 02134
Boston +1 617 555 0143
London +44 20 7946 0381
Sydney +61 2 5550 1296
www.thornfieldvisagroup.example
ghensworth@thornfieldvisagroup.example
United States Immigration and Tax Counsel

```html
<!DOCTYPE html>
<html lang="en">
<head>
<meta charset="utf-8">
<title>Thornfield Visa Group – Business Card</title>
<link rel="stylesheet" href="https://fonts.googleapis.com/css2?family=Oswald:wght@300;400;500&display=swap">
<style>
  :root {
    --backdrop: #2a2a2a;
    --navy: #141a52;
    --navy-deep: #0b0f3a;
    --navy-light: #1f2a72;
    --accent: #1f86c0;
    --accent-light: #2ea3d6;
    --paper: #f3f3f3;
    --ink: #3a3f55;
    --white: #ffffff;
  }
  * { margin: 0; padding: 0; box-sizing: border-box; }
  html, body { width: 1200px; height: 588px; overflow: hidden; }
  body {
    position: relative;
    background: var(--backdrop);
    font-family: "Oswald", "Arial Narrow", sans-serif;
  }
  .card {
    position: absolute;
    top: 187px;
    width: 393px;
    height: 223px;
    border-radius: 14px;
    overflow: hidden;
  }

  /* Front */
  .card-front {
    left: 157px;
    background: linear-gradient(160deg, var(--navy-light) 0%, var(--navy) 45%, var(--navy-deep) 100%);
  }
  .front-brand {
    position: absolute;
    left: 64px;
    top: 84px;
    display: flex;
    align-items: center;
    gap: 12px;
  }
  .brand-square {
    width: 40px;
    height: 40px;
    background: var(--accent);
  }
  .front-brand .brand-name {
    color: var(--white);
    font-weight: 400;
    font-size: 27px;
    letter-spacing: 0.5px;
    line-height: 1;
  }
  .front-web {
    position: absolute;
    left: 0; right: 0;
    top: 187px;
    text-align: center;
    color: var(--white);
    font-size: 9.5px;
    letter-spacing: 2.2px;
    text-transform: uppercase;
  }
  .front-web .tld { color: var(--accent-light); }

  /* Back */
  .card-back {
    left: 660px;
    background: var(--paper);
  }
  .back-brand {
    position: absolute;
    right: 25px;
    top: 26px;
    display: flex;
    align-items: center;
    gap: 10px;
  }
  .back-brand .brand-square {
    width: 46px;
    height: 46px;
    background: var(--navy);
  }
  .back-brand .brand-name {
    color: var(--navy);
    font-weight: 400;
    font-size: 19px;
    line-height: 1.05;
    width: 140px;
  }
  .holder-name {
    position: absolute;
    left: 37px;
    top: 127px;
    color: var(--accent);
    font-weight: 500;
    font-size: 11.5px;
  }
  .rule {
    position: absolute;
    left: 35px;
    right: 25px;
    top: 152px;
    height: 1px;
    background: var(--navy);
  }
  .contact {
    position: absolute;
    top: 162px;
    font-size: 6.6px;
    line-height: 13px;
    color: var(--ink);
    font-weight: 300;
  }
  .contact-address { left: 24px; }
  .contact-address .firm { color: var(--accent); font-weight: 500; }
  .contact-offices { left: 152px; }
  .contact-direct { left: 258px; }
  .contact .row { display: flex; align-items: center; white-space: nowrap; }
  .contact .city { width: 30px; color: var(--accent); font-weight: 500; }
  .contact .icon { width: 13px; height: 9px; flex: none; }
  .contact .indent { padding-left: 13px; }
  .icon path, .icon rect, .icon circle { fill: var(--accent); }
  .tagline-band {
    position: absolute;
    left: 0;
    bottom: 0;
    width: 365px;
    height: 13px;
    background: var(--navy);
    color: var(--white);
    font-size: 8.2px;
    letter-spacing: 1px;
    line-height: 13px;
    padding-left: 37px;
    white-space: nowrap;
  }
  .band-tab {
    position: absolute;
    right: 0;
    bottom: 0;
    width: 28px;
    height: 13px;
    background: var(--accent-light);
  }
</style>
</head>
<body>

<section class="card card-front" aria-label="Card front">
  <div class="front-brand">
    <div class="brand-square"></div>
    <span class="brand-name">Thornfield Visa Group</span>
  </div>
  <p class="front-web">www.thornfieldvisagroup<span class="tld">.example</span></p>
</section>

<section class="card card-back" aria-label="Card back">
  <div class="back-brand">
    <div class="brand-square"></div>
    <span class="brand-name">Thornfield Visa Group</span>
  </div>

  <h1 class="holder-name">Gerald T. Hensworth, Esq. LL.M, M.Sc., M.Fin</h1>
  <div class="rule"></div>

  <div class="contact contact-address">
    <div class="row">
      <svg class="icon" viewBox="0 0 13 9" aria-hidden="true"><path d="M4 0a3 3 0 0 0-3 3c0 2.2 3 6 3 6s3-3.8 3-6a3 3 0 0 0-3-3zm0 4.2A1.2 1.2 0 1 1 4 1.8a1.2 1.2 0 0 1 0 2.4z"/></svg>
      <span class="firm">Thornfield Visa Group LLC</span>
    </div>
    <div class="row indent">47 Kessel Ave., #218</div>
    <div class="row indent">Boston, MA 02134</div>
  </div>

  <div class="contact contact-offices">
    <div class="row"><span class="city">Boston</span>+1 617 555 0143</div>
    <div class="row"><span class="city">London</span>+44 20 7946 0381</div>
    <div class="row"><span class="city">Sydney</span>+61 2 5550 1296</div>
  </div>

  <div class="contact contact-direct">
    <div class="row">
      <svg class="icon" viewBox="0 0 13 9" aria-hidden="true"><path d="M2 0h4.5v9H2zM2.8 1v6.2h2.9V1z"/></svg>
      +44 20 7946 0381
    </div>
    <div class="row">
      <svg class="icon" viewBox="0 0 13 9" aria-hidden="true"><path d="M0.5 3.2C1.5 1.5 7.5 1.5 8.5 3.2L7.4 4.4 6 3.6V3H3v.6l-1.4.8zM2 5h5l.6 3.5H1.4z"/></svg>
      +44 20 7946 0381
    </div>
    <div class="row">
      <svg class="icon" viewBox="0 0 13 9" aria-hidden="true"><path d="M0.5 2h8v5.5h-8zM1.2 2.6l3.3 2.4 3.3-2.4v-.3H1.2z"/></svg>
      ghensworth@thornfieldvisagroup.example
    </div>
  </div>

  <p class="tagline-band">UNITED STATES IMMIGRATION AND TAX COUNSEL</p>
  <div class="band-tab"></div>
</section>

</body>
</html>
```